Zestmora website needs a desktop homepage design

We need a desktop homepage design for Zestmora.co.uk, a website to help you to find the best restaurants in each main city of Europe, with initial focus on London. It is not a directory with thousands of restaurants and reviews, else lists of top 20 restaurants for each area of the city. Zestmora from all around the city will be able to keep an itinerary of where they eat, showing them later funny stats like "this month you really went for pizzas, don't you?". Keep it funny but professional.

A bit of branding has been done but this project give you total freedom to design the homepage of the site. The design must be a mix between minimal, flat and clean layout. The main idea is to keep it simple, easy to use and showing just the necessary elements.

For the font and colour scheme, we would like to use a thin but energetic font using the #E1393A colour as starting point even if you have freedom to slightly modify it. Blacks, greys and whites can be the secondary colours but we are open to introduce another main colour to the site like green, orange or yellow.

A simple wireframe has been attached to help you but the main elements that the page requires are the next:
- Panoramic fancy image in the header to contain the logo and the search form (the fields of the form are specified on the wireframe) and maybe some animated text to fill the right gap.
- List of results (10 results per page) showing the main info for each restaurant: name, thumbnail, location (zone, area), category, price, description, rating (no with stars please) and whatever you want to add that makes sense.
- Right hand sidebar with 3 widgets: Categories, Location and prices.

You can get the icons from vendrako.net.

We are open to have some text-shadows, rounded corners, box-shadows but trying to keep it minimal, flat and clean as much as possible. The main attractive of the site are the food/restaurant images.

Target Market(s)

22 - 45 Zestmora lovers from the city. busy people that want to disconnect and relax through the food. The don't mind to pay for quality and new experiences. Up to meet new places around them.

Industry/Entity Type

Restaurant

Requirements
Must have
• Panoramic image in the header, restaurants search form as per wireframe, list results with pagination, right hand sidebar with the widgets mention above and a nice footer with extra elements like "latest restaurants, latest tweets, etc.."
Nice to have
• This site will only be supported by the latest browsers so the idea is to have nice CSS3 transitions all around. Have that in mind at the time to design it even if you cannot show it on the design.
Should not have
• Busy backgrounds and unnecessary images that would slow down the page load.

```html
<!DOCTYPE html>
<html lang="en">
<head>
<meta charset="utf-8">
<title>Zestmora – Best Restaurants in London</title>
<link href="https://fonts.googleapis.com/css2?family=Roboto:wght@300;400;500&display=swap" rel="stylesheet">
<style>
:root{
  --red:#e1393a;
  --red-soft:#e45556;
  --green:#6cb74b;
  --ink:#333;
  --text:#555;
  --muted:#888;
  --line:#d9d9d9;
  --page:#eeeeee;
  --side:#f3f3f3;
  --white:#fff;
}
*{box-sizing:border-box;margin:0;padding:0}
html,body{width:976px;height:1200px;overflow:hidden;background:var(--page)}
body{font-family:'Roboto',Arial,sans-serif;color:var(--ink)}
.page{position:relative;width:1200px;height:1475px;transform:scale(.81333);transform-origin:0 0;overflow:hidden;background:var(--page)}
.abs{position:absolute}

.topbar{left:0;top:0;width:1200px;height:57px;background:var(--white);border-bottom:1px solid #e2e2e2}
.brand{left:112px;top:10px;font-size:34px;font-weight:500;color:var(--red);letter-spacing:-1px;display:flex;align-items:center;gap:8px}
.brand-dot{width:14px;height:14px;background:var(--red);border-radius:50%}

.hero{left:0;top:57px;width:1200px;height:558px;background:
  radial-gradient(ellipse at 75% 30%,#dfe8d4 0%,#b9cf86 25%,transparent 55%),
  radial-gradient(ellipse at 30% 75%,#7a3a1e 0%,#4f2414 40%,transparent 70%),
  linear-gradient(100deg,#5d2a17 0%,#8a4a25 35%,#9fb45a 60%,#c7d69a 80%,#a53a25 100%)}
.hero-copy{right:110px;top:250px;text-align:right;color:var(--white);text-shadow:0 2px 4px rgba(0,0,0,.6)}
.hero-copy h1{font-size:41px;font-weight:500;margin-bottom:14px}
.hero-copy p{font-size:26px;font-weight:300;line-height:33px;width:490px;margin-left:auto}

.search{left:110px;top:106px;width:400px;height:461px;background:rgba(235,235,235,.93);box-shadow:0 1px 4px rgba(0,0,0,.3)}
.search-head{height:62px;background:var(--red-soft);color:var(--white);font-size:26px;font-weight:300;padding:18px 0 0 43px}
.search form{padding:22px 40px 0 40px}
.field-label{display:block;font-size:15px;font-weight:300;color:#333;margin:0 0 5px 2px}
.field-label .req{color:var(--red)}
.field{position:relative;height:40px;background:var(--white);border:1px solid #ccc;font-size:15px;font-style:italic;font-weight:300;color:#999;padding:11px 13px;margin-bottom:13px}
.field .ctl{position:absolute;right:0;top:10px;width:34px;height:20px;border-left:1px solid #ccc;display:flex;align-items:center;justify-content:center}
.find-btn{display:block;width:319px;height:54px;margin:8px 0 0 2px;background:var(--green);border:1px solid #58a03a;color:var(--white);font-family:inherit;font-size:21px;font-weight:400}

.section-bar{left:0;top:615px;width:1200px;height:63px;background:var(--white);border-bottom:1px solid #e3e3e3}
.section-bar h2{position:absolute;left:131px;top:18px;font-size:26px;font-weight:300;display:flex;align-items:center;gap:12px;color:#222}
.section-bar h2 em{font-style:normal;color:var(--red)}

.sidebar-bg{left:840px;top:679px;width:360px;height:800px;background:var(--side);border-left:2px solid #e2e2e2}

.card{left:110px;width:710px;height:163px;background:var(--white);border:1px solid #e0e0e0}
.thumb{position:absolute;left:20px;top:20px;width:172px;height:123px;background:linear-gradient(135deg,#7a4a14,#d39a2c 40%,#f0d47a 55%,#9a5a18 80%,#4a2a0c)}
.card h3{position:absolute;left:210px;top:20px;font-size:16px;font-weight:400;color:#222}
.rating{position:absolute;right:18px;top:21px;display:flex;gap:3px}
.card .rule{position:absolute;left:210px;right:18px;top:49px;border-top:1px dotted #bbb}
.card p{position:absolute;left:211px;right:18px;top:60px;font-size:12.5px;font-weight:300;line-height:18px;color:#444;text-align:justify}
.meta{position:absolute;left:211px;top:127px;display:flex;gap:18px;font-size:12px;font-weight:300;color:#333}
.meta span{display:flex;align-items:center;gap:4px}

.widget{left:865px;width:225px;background:var(--white);border:1px solid #e0e0e0}
.widget-head{height:50px;background:var(--red);color:var(--white);font-size:18px;display:flex;align-items:center}
.widget-head .ico{width:48px;display:flex;justify-content:center;border-right:1px solid rgba(255,255,255,.5);height:26px;align-items:center}
.widget-head span.t{padding-left:13px}
.widget ul{list-style:none;padding:9px 19px 6px 21px}
.widget li{display:flex;gap:16px;border-bottom:1px dotted #ccc;padding:10px 0;font-size:14px;font-weight:300;color:#333}
.widget li:last-child{border-bottom:0}
.widget.prices li{padding:11px 0 10px}
.widget li .n{width:12px;height:12px;background:#444;color:#fff;font-size:8px;display:flex;align-items:center;justify-content:center;margin-top:3px;flex:none}
.widget li small{display:block;font-size:11.5px;color:var(--muted);margin-top:1px}
</style>
</head>
<body>
<div class="page">
<svg width="0" height="0" style="position:absolute">
  <defs>
    <symbol id="hat" viewBox="0 0 16 16"><circle cx="4" cy="6" r="3.6"/><circle cx="8" cy="4.5" r="4"/><circle cx="12" cy="6" r="3.6"/><rect x="3.5" y="7" width="9" height="5"/><rect x="3.5" y="12.8" width="9" height="2.4"/></symbol>
    <symbol id="pin" viewBox="0 0 10 14"><path d="M5 0a4.5 4.5 0 0 0-4.5 4.5C.5 8 5 14 5 14s4.5-6 4.5-9.5A4.5 4.5 0 0 0 5 0zm0 6.3a1.8 1.8 0 1 1 0-3.6 1.8 1.8 0 0 1 0 3.6z"/></symbol>
    <symbol id="cross" viewBox="0 0 14 14"><path d="M2 1l11 11-1.4 1.4L.6 2.4zM12 1l1.4 1.4-11 11L1 12z"/></symbol>
    <symbol id="tag" viewBox="0 0 14 14"><path d="M7 0h7v7l-7 7-7-7zm4 2.2a1 1 0 1 0 0 2 1 1 0 0 0 0-2z"/></symbol>
  </defs>
</svg>

<header class="abs topbar">
  <div class="abs brand"><span class="brand-dot"></span>Zestmora</div>
</header>

<section class="abs hero" role="img" aria-label="Close-up photo of grilled meat, roasted onion, salad and a yogurt dip"></section>
<div class="abs hero-copy">
  <h1>Find some awesome food!</h1>
  <p>Lorem ipsum dolor sit amet consectetur adipiscing elit usce non dui tortorenim elit scelerisque non sem porta ultricies</p>
</div>

<aside class="abs search">
  <div class="search-head">Zestmora in London</div>
  <form>
    <label class="field-label">What restaurant?</label>
    <div class="field">Mushu<span class="ctl"><svg width="11" height="11" fill="#aaa"><use href="#cross"/></svg></span></div>
    <label class="field-label">What kind of food?</label>
    <div class="field">All<span class="ctl"><svg width="9" height="5" fill="#999"><path d="M0 0h9L4.5 5z"/></svg></span></div>
    <label class="field-label">Where?</label>
    <div class="field">Everywhere</div>
    <label class="field-label">Prices? <span class="req">*</span></label>
    <div class="field">All</div>
    <button type="button" class="find-btn">Find now!</button>
  </form>
</aside>

<div class="abs section-bar">
  <h2><svg width="22" height="22" fill="#e1393a"><use href="#hat"/></svg><span>Best Restaurants in <em>London</em></span></h2>
</div>

<div class="abs sidebar-bg"></div>

<article class="abs card" style="top:719px">
  <div class="thumb" role="img" aria-label="Restaurant dining room with set tables"></div>
  <h3>Lorem ipsum restaurant</h3>
  <div class="rating"><svg width="16" height="16" fill="#e1393a"><use href="#hat"/></svg><svg width="16" height="16" fill="#e1393a"><use href="#hat"/></svg><svg width="16" height="16" fill="#e1393a"><use href="#hat"/></svg><svg width="16" height="16" fill="#e1393a"><use href="#hat"/></svg><svg width="16" height="16" fill="#bbb"><use href="#hat"/></svg></div>
  <div class="rule"></div>
  <p>Lorem ipsum dolor sit amet, consectetur adipiscing elit. Fusce non dui elit. Etiam at urna ut tortor varius gravida ut ut neque. Quisque adipiscing mattis nunc sit amet varius. Maecenas et sodales massa.</p>
  <div class="meta"><span><svg width="8" height="12" fill="#e1393a"><use href="#pin"/></svg>Halden Row, Southwark</span><span><svg width="11" height="11" fill="#e1393a"><use href="#cross"/></svg>Organic food</span><span><svg width="12" height="12" fill="#e1393a"><use href="#tag"/></svg>£5 - £100</span></div>
</article>

<article class="abs card" style="top:892px">
  <div class="thumb" role="img" aria-label="Restaurant dining room with set tables"></div>
  <h3>Lorem ipsum restaurant</h3>
  <div class="rating"><svg width="16" height="16" fill="#e1393a"><use href="#hat"/></svg><svg width="16" height="16" fill="#e1393a"><use href="#hat"/></svg><svg width="16" height="16" fill="#e1393a"><use href="#hat"/></svg><svg width="16" height="16" fill="#e1393a"><use href="#hat"/></svg><svg width="16" height="16" fill="#bbb"><use href="#hat"/></svg></div>
  <div class="rule"></div>
  <p>Lorem ipsum dolor sit amet, consectetur adipiscing elit. Fusce non dui elit. Etiam at urna ut tortor varius gravida ut ut neque. Quisque adipiscing mattis nunc sit amet varius. Maecenas et sodales massa.</p>
  <div class="meta"><span><svg width="8" height="12" fill="#e1393a"><use href="#pin"/></svg>Halden Row, Southwark</span><span><svg width="11" height="11" fill="#e1393a"><use href="#cross"/></svg>Organic food</span><span><svg width="12" height="12" fill="#e1393a"><use href="#tag"/></svg>£5 - £100</span></div>
</article>

<article class="abs card" style="top:1065px">
  <div class="thumb" role="img" aria-label="Restaurant dining room with set tables"></div>
  <h3>Lorem ipsum restaurant</h3>
  <div class="rating"><svg width="16" height="16" fill="#e1393a"><use href="#hat"/></svg><svg width="16" height="16" fill="#e1393a"><use href="#hat"/></svg><svg width="16" height="16" fill="#e1393a"><use href="#hat"/></svg><svg width="16" height="16" fill="#e1393a"><use href="#hat"/></svg><svg width="16" height="16" fill="#bbb"><use href="#hat"/></svg></div>
  <div class="rule"></div>
  <p>Lorem ipsum dolor sit amet, consectetur adipiscing elit. Fusce non dui elit. Etiam at urna ut tortor varius gravida ut ut neque. Quisque adipiscing mattis nunc sit amet varius. Maecenas et sodales massa.</p>
  <div class="meta"><span><svg width="8" height="12" fill="#e1393a"><use href="#pin"/></svg>Halden Row, Southwark</span><span><svg width="11" height="11" fill="#e1393a"><use href="#cross"/></svg>Organic food</span><span><svg width="12" height="12" fill="#e1393a"><use href="#tag"/></svg>£5 - £100</span></div>
</article>

<article class="abs card" style="top:1238px">
  <div class="thumb" role="img" aria-label="Restaurant dining room with set tables"></div>
  <h3>Lorem ipsum restaurant</h3>
  <div class="rating"><svg width="16" height="16" fill="#e1393a"><use href="#hat"/></svg><svg width="16" height="16" fill="#e1393a"><use href="#hat"/></svg><svg width="16" height="16" fill="#e1393a"><use href="#hat"/></svg><svg width="16" height="16" fill="#e1393a"><use href="#hat"/></svg><svg width="16" height="16" fill="#bbb"><use href="#hat"/></svg></div>
  <div class="rule"></div>
  <p>Lorem ipsum dolor sit amet, consectetur adipiscing elit. Fusce non dui elit. Etiam at urna ut tortor varius gravida ut ut neque. Quisque adipiscing mattis nunc sit amet varius. Maecenas et sodales massa.</p>
  <div class="meta"><span><svg width="8" height="12" fill="#e1393a"><use href="#pin"/></svg>Halden Row, Southwark</span><span><svg width="11" height="11" fill="#e1393a"><use href="#cross"/></svg>Organic food</span><span><svg width="12" height="12" fill="#e1393a"><use href="#tag"/></svg>£5 - £100</span></div>
</article>

<article class="abs card" style="top:1411px">
  <div class="thumb" role="img" aria-label="Restaurant dining room with set tables"></div>
  <h3>Lorem ipsum restaurant</h3>
  <div class="rating"><svg width="16" height="16" fill="#e1393a"><use href="#hat"/></svg><svg width="16" height="16" fill="#e1393a"><use href="#hat"/></svg><svg width="16" height="16" fill="#e1393a"><use href="#hat"/></svg><svg width="16" height="16" fill="#e1393a"><use href="#hat"/></svg><svg width="16" height="16" fill="#bbb"><use href="#hat"/></svg></div>
  <div class="rule"></div>
</article>

<section class="abs widget" style="top:719px">
  <div class="widget-head"><span class="ico"><svg width="18" height="18" fill="#fff"><use href="#cross"/></svg></span><span class="t">Categories</span></div>
  <ul>
    <li><span class="n">3</span>Italian restaurants</li>
    <li><span class="n">2</span>Indian restaurants</li>
    <li><span class="n">4</span>Chinese restaurants</li>
    <li><span class="n">3</span>Greek restaurants</li>
    <li><span class="n">3</span>French restaurants</li>
  </ul>
</section>

<section class="abs widget" style="top:980px">
  <div class="widget-head"><span class="ico"><svg width="12" height="17" fill="#fff"><use href="#pin"/></svg></span><span class="t">Locations</span></div>
  <ul>
    <li><span class="n">3</span>West London</li>
    <li><span class="n">2</span>East London</li>
    <li><span class="n">4</span>South London</li>
    <li><span class="n">3</span>North London</li>
  </ul>
</section>

<section class="abs widget prices" style="top:1204px">
  <div class="widget-head"><span class="ico"><svg width="17" height="17" fill="#fff"><use href="#tag"/></svg></span><span class="t">Prices</span></div>
  <ul>
    <li><span class="n">3</span><span>Casual restaurants<small>£10 - £20</small></span></li>
    <li><span class="n">3</span><span>Casual restaurants<small>£10 - £20</small></span></li>
    <li><span class="n">3</span><span>Casual restaurants<small>£10 - £20</small></span></li>
  </ul>
</section>
</div>
</body>
</html>
```